Bref créative
Brightpath Outcomes Inc
I need double sided standard sized Business Card [3.5" x 2"]
You decid
Professional
Danielle Hartwell
CEO
4172 Juniper Ridge Drive,
Suite 517
Lakemont Springs, ST 48109
danielle.hartwell@brightpathoutcomes.example
www.brightpathoutcomes.example
On the back of the card we want another web adrdress of
walkingherownroute.example

```html
<!DOCTYPE html>
<html lang="en">
<head>
<meta charset="utf-8">
<title>Brightpath Outcomes Inc – Stationery</title>
<link href="https://fonts.googleapis.com/css2?family=Roboto:wght@400;700&display=swap" rel="stylesheet">
<style>
  :root {
    --backdrop: #c8c8ca;
    --paper: #ffffff;
    --charcoal: #3a393b;
    --brand-red: #e8453c;
    --ink: #555457;
    --soft-ink: #d8d8d8;
  }
  * { box-sizing: border-box; margin: 0; padding: 0; }
  html, body { width: 1200px; height: 655px; overflow: hidden; }
  body {
    background: var(--backdrop);
    font-family: "Roboto", Arial, sans-serif;
    color: var(--ink);
    position: relative;
  }
  .sheet { position: absolute; background: var(--paper); box-shadow: 0 1px 3px rgba(0,0,0,.18); overflow: hidden; }

  .wordmark { display: flex; align-items: center; gap: 6px; position: absolute; }
  .wordmark__square { width: 14px; height: 14px; background: var(--brand-red); flex: none; }
  .wordmark__name { font-weight: 700; text-transform: uppercase; line-height: 1.05; letter-spacing: .3px; white-space: nowrap; }
  .wordmark--dark .wordmark__name { color: var(--charcoal); }
  .wordmark--light .wordmark__name { color: var(--paper); }

  .small { font-size: 6px; line-height: 1.55; color: var(--ink); white-space: nowrap; }
  .small--light { color: var(--soft-ink); }

  .letterhead { left: 187px; top: 31px; width: 408px; height: 588px; }
  .letterhead .wordmark { left: 22px; top: 14px; }
  .letterhead .wordmark__name { font-size: 12px; }
  .letterhead__web { position: absolute; right: 26px; top: 16px; }
  .letterhead__contact { position: absolute; left: 22px; bottom: 10px; }

  .card-back { left: 96px; top: 206px; width: 211px; height: 113px; background: var(--brand-red); }
  .card-back__web { position: absolute; right: 10px; top: 9px; color: var(--paper); font-size: 6px; white-space: nowrap; }

  .card-front { left: 96px; top: 326px; width: 211px; height: 106px; background: var(--charcoal); }
  .card-front .wordmark { left: 10px; top: 10px; gap: 4px; }
  .card-front .wordmark__square { width: 9px; height: 9px; }
  .card-front .wordmark__name { font-size: 7.5px; }
  .card-front__contact { position: absolute; left: 10px; top: 46px; font-size: 4.6px; }
  .card-front__person { position: absolute; right: 10px; top: 66px; text-align: right; }
  .card-front__name { color: var(--brand-red); font-size: 8px; font-weight: 400; white-space: nowrap; }
  .card-front__title { color: var(--paper); font-size: 6px; margin-top: 2px; }
  .card-front__email { position: absolute; left: 10px; bottom: 7px; font-size: 4.6px; }

  .envelope-back { left: 660px; top: 79px; width: 516px; height: 204px; }
  .envelope-back__flap { position: absolute; left: 0; top: 0; }
  .envelope-back .wordmark { left: 190px; top: 30px; }
  .envelope-back .wordmark__name { font-size: 12px; }

  .envelope-front { left: 660px; top: 343px; width: 516px; height: 276px; }
  .envelope-front__band { position: absolute; left: 0; top: 0; width: 100%; height: 89px; background: var(--charcoal); }
  .envelope-front .wordmark { left: 18px; top: 30px; }
  .envelope-front .wordmark__name { font-size: 12px; }
  .envelope-front__web { position: absolute; right: 22px; top: 14px; }
  .envelope-front__contact { position: absolute; left: 26px; top: 150px; }
</style>
</head>
<body>

  <section class="sheet letterhead" aria-label="Letterhead">
    <div class="wordmark wordmark--dark">
      <span class="wordmark__square"></span>
      <span class="wordmark__name">Brightpath<br>Outcomes Inc</span>
    </div>
    <p class="small letterhead__web">www.brightpathoutcomes.example</p>
    <div class="small letterhead__contact">
      <p>Ph: 555-210-0142</p>
      <p>Fax: 555-210-0143</p>
      <p>danielle.hartwell@brightpathoutcomes.example</p>
      <p>4172 Juniper Ridge Drive, Suite 517 Lakemont Springs, ST 48109</p>
    </div>
  </section>

  <section class="sheet card-back" aria-label="Business card back">
    <p class="card-back__web">www.walkingherownroute.example</p>
  </section>

  <section class="sheet card-front" aria-label="Business card front">
    <div class="wordmark wordmark--light">
      <span class="wordmark__square"></span>
      <span class="wordmark__name">Brightpath<br>Outcomes Inc</span>
    </div>
    <div class="small small--light card-front__contact">
      <p>Ph: 555-210-0142</p>
      <p>Fax: 555-210-0143</p>
      <p>4172 Juniper Ridge Drive, Suite 517</p>
      <p>Lakemont Springs, ST 48109</p>
    </div>
    <div class="card-front__person">
      <p class="card-front__name">Danielle Hartwell</p>
      <p class="card-front__title">CEO</p>
    </div>
    <p class="small small--light card-front__email">danielle.hartwell@brightpathoutcomes.example</p>
  </section>

  <section class="sheet envelope-back" aria-label="Envelope back">
    <svg class="envelope-back__flap" width="516" height="204" viewBox="0 0 516 204" aria-hidden="true">
      <path d="M0 0 H516 V52 H330 C300 52 290 108 258 108 C226 108 216 52 186 52 H0 Z" fill="var(--charcoal)"/>
    </svg>
    <div class="wordmark wordmark--light">
      <span class="wordmark__square"></span>
      <span class="wordmark__name">Brightpath<br>Outcomes Inc</span>
    </div>
  </section>

  <section class="sheet envelope-front" aria-label="Envelope front">
    <div class="envelope-front__band"></div>
    <div class="wordmark wordmark--light">
      <span class="wordmark__square"></span>
      <span class="wordmark__name">Brightpath<br>Outcomes Inc</span>
    </div>
    <p class="small small--light envelope-front__web">www.brightpathoutcomes.example</p>
    <div class="small envelope-front__contact">
      <p>Ph: 555-210-0142</p>
      <p>Fax: 555-210-0143</p>
      <p>danielle.hartwell@brightpathoutcomes.example</p>
      <p>4172 Juniper Ridge Drive, Suite 517 Lakemont Springs, ST 48109</p>
    </div>
  </section>

</body>
</html>
```